small brochure design

I have the basic content for a brochure to describe my business services - I will need someone to take this content & elaborate and re format into something well presentable?

The logo for the business is the KTLV logo.
It should be a gold colour on black
Please feel free to change background colour and whatever you feel to make more attractive..

Looking for a small brochure 84 which is 8 printed pages including front back covers.

Can you please source & use relevant images for the topic & of my industry to use.
with content aroud the images - i.e. https://www.lumavexo.com.au/find?q=stone+masonry&safe=off&client=bravik-b&hs=KuT&rls=net.tovalen:en-GB:default&source=pqwd&tbm=pics&sa=Y&ei=wmtkHpL2R8-3nBgtrfQHxZA&ved=2TzMW_BrpOQ&biw=1760&bih=883

This will be used as a introduction of services –

The back inside page should be a contact page and a closing statement – I have also attached a copy of one we use that you can use as an example.

Once this is complete we will refine the content to be used in other items such as presentation folders etc … which we will get you to help create

Please contact me via email and ensure that you CC dulwa582@fernpost.net so that my marketing manager can be across it also.

Thanks

Target Market(s)

Real Estates
Strata
Councils & Government
Herritage

Industry/Entity Type

Marketing

Requirements
Must have
• Contact Page
Examples of jobs
Lots of quality photos

```html
<!DOCTYPE html>
<html lang="en">
<head>
<meta charset="utf-8">
<title>KTLV Stonemasonry – Brochure Spread</title>
<link rel="stylesheet" href="https://fonts.googleapis.com/css2?family=Great+Vibes&family=Open+Sans:wght@400;600&display=swap">
<style>
  :root{
    --gold:#c0913c;
    --gold-light:#e6c27a;
    --ink:#141414;
    --black:#000;
    --paper:#fff;
    --stage:#3a3a3a;
    --sky-top:#8fa2c8;
    --sky-low:#e8ecf5;
    --stone:#8a7a66;
  }
  *{box-sizing:border-box;margin:0;padding:0}
  html,body{width:1186px;height:1200px;overflow:hidden;background:var(--stage)}
  body{position:relative;font-family:"Open Sans",Arial,sans-serif;color:var(--ink)}
  .spread{position:absolute;left:71px;top:195px;width:1044px;height:810px;background:var(--black)}
  .page{position:absolute;left:12px;top:10px;width:1020px;height:790px;background:var(--paper);overflow:hidden}
  .header-band{position:absolute;left:0;top:0;width:1020px;height:130px}
  .section-title{position:absolute;top:18px;font-family:"Great Vibes",cursive;font-size:42px;color:var(--ink);font-weight:400;white-space:nowrap}
  .title-goal{left:26px}
  .title-service{left:428px}
  .title-packages{left:712px}
  .column{position:absolute;font-size:12.4px;line-height:17px}
  .column p{margin-bottom:17px}
  .col-goal{left:16px;top:145px;width:302px;text-align:justify}
  .col-goal .lead{font-size:19px;line-height:27px;text-align:left;margin-bottom:18px}
  .col-service{left:354px;top:152px;width:315px;text-align:justify}
  .col-service .big{font-size:17px}
  .col-packages{left:707px;top:158px;width:295px;font-size:12px;line-height:15.5px}
  .col-packages p{margin-bottom:15px}
  .price{font-size:22px;font-weight:600;color:var(--gold);line-height:15px}
  .photo{position:absolute}
  .hero{left:0;top:362px;width:693px;height:410px;background:linear-gradient(180deg,var(--sky-top) 0%,var(--sky-low) 35%,#b8ab97 60%,var(--stone) 100%)}
  .thumb{border:1px solid #222;background:linear-gradient(160deg,#9d9384,#5c5448)}
  .stairs{left:15px;top:443px;width:124px;height:120px}
  .worker{left:165px;top:502px;width:124px;height:120px;background:linear-gradient(160deg,#a0634a,#c9c2b6)}
  .wall-ba{left:28px;top:608px;width:123px;height:103px;background:linear-gradient(180deg,#8d9a6a,#d8d2c4)}
  .window-a{left:710px;top:495px;width:96px;height:118px;background:linear-gradient(90deg,#b48a70,#2a2a2a)}
  .window-b{left:815px;top:502px;width:104px;height:128px;background:linear-gradient(90deg,#b08c78,#1e1e1e)}
  .wall-right{left:693px;top:560px;width:327px;height:190px;background:linear-gradient(180deg,var(--paper) 0%,var(--paper) 45%,#7c7060 60%,#3f3a33 100%)}
  .tag{position:absolute;background:var(--black);color:var(--paper);font-size:12px;line-height:17px;padding:0 14px;white-space:nowrap}
  .tag-left{left:28px;top:590px;width:123px}
  .tag-right{left:710px;top:477px;width:121px}
  .footer-wave{position:absolute;left:0;top:700px;width:1020px;height:90px}
  .book-now{position:absolute;left:705px;top:748px;font-size:25px;color:var(--gold);white-space:nowrap}
</style>
</head>
<body>
<div class="spread">
  <div class="page">
    <svg class="header-band" viewBox="0 0 1020 130" aria-hidden="true">
      <defs>
        <linearGradient id="sheen" x1="0" x2="1">
          <stop offset="0" stop-color="#fff"/>
          <stop offset=".5" stop-color="#f3dfb5"/>
          <stop offset="1" stop-color="#fff"/>
        </linearGradient>
      </defs>
      <path d="M0 0H1020V82C870 110 700 118 520 98C330 76 160 70 0 110Z" fill="#c0913c"/>
      <path d="M0 110C160 70 330 76 520 98C700 118 870 110 1020 82V92C870 124 700 130 520 108C330 88 160 84 0 124Z" fill="url(#sheen)"/>
    </svg>
    <h2 class="section-title title-goal">Our Goal</h2>
    <h2 class="section-title title-service">Our Service</h2>
    <h2 class="section-title title-packages">Work and Packages</h2>

    <div class="photo hero" role="img" aria-label="Photo of a heritage stone cottage with slate roof under a blue sky"></div>
    <div class="photo wall-right" role="img" aria-label="Photo of a restored stone garden wall with a lamp post on a pillar"></div>

    <section class="column col-goal">
      <p class="lead">Our aim in pitching our product is not only to benefit us but to add value to your properties .</p>
      <p>As we all know when it comes to real estate or selling any product for that matter it usually all comes down to image and quality.</p>
      <p>The simple cleaning and maintenance of property may raise its potential value by thousands especially when considering aesthetics.</p>
      <p style="text-align:left">That's why we are here to provide you with unbeatable quality and packages on all our stone work.</p>
    </section>

    <section class="column col-service">
      <p><span class="big">We at KTLV</span> are here to provide you with an extensive service on all your property stone work maintenance needs.</p>
      <p>Being a fifth Generation stonemason myself I have been able to provide many services and contributions to major Sydney buildings such as the Australian Harbour Arcade building, Carrow town hall and even St. Alden's Cathedral.</p>
      <p>A few things we specialise in are Heritage, Restoration, cleaning and maintenance of all stone works and even other odd bits and pieces such as pavers concrete.</p>
    </section>

    <section class="column col-packages">
      <p>On the following page there are some images that will be able to provide you with more assistance on the kind of works our team carries out.</p>
      <p>Our Packages for repointing and cleaning of the stone consist of chopping out the original damaged parts. Refilling them with a sand and cement based mortar cleaning and washing the stone back down to it's original state without damaging the original works.</p>
      <p>This package starts from <span class="price">$150</span><br>per square metre for regular coursed walls.<br>As shown in the pictures.</p>
      <p>For replacement of stones and indents our<br><br>package starts from <span class="price">$350</span> per stone which includes supply and installation of materials.</p>
    </section>

    <div class="photo thumb stairs" role="img" aria-label="Photo of restored sandstone stairs"></div>
    <div class="photo thumb worker" role="img" aria-label="Photo of a stonemason repointing a wall base"></div>
    <div class="tag tag-left">Before and after</div>
    <div class="photo thumb wall-ba" role="img" aria-label="Before and after photo of a cleaned sandstone block wall"></div>
    <div class="tag tag-right">Before and after</div>
    <div class="photo thumb window-a" role="img" aria-label="Before photo of damaged stone beside a window"></div>
    <div class="photo thumb window-b" role="img" aria-label="After photo of repaired stone beside a window"></div>

    <svg class="footer-wave" viewBox="0 0 1020 90" aria-hidden="true">
      <path d="M0 12C140 60 300 70 470 52C640 34 820 18 1020 40V90H0Z" fill="#000"/>
      <path d="M0 12C140 60 300 70 470 52C640 34 820 18 1020 40" fill="none" stroke="#c0913c" stroke-width="4"/>
      <path d="M120 60C300 80 520 52 700 42C820 36 920 42 1020 50" fill="none" stroke="#c0913c" stroke-width="2" opacity=".7"/>
    </svg>
    <div class="book-now">Book Now 0491 570 318</div>
  </div>
</div>
</body>
</html>
```